Quite like thee: needs a logo design and a business card

The business name is called: Quite like thee. It's all about fashion for everyone who needs to gain confidence and find his own style: Image Consultant, Personal Shopper. Here my Facebook fan page: https://www.facebook.com/pages/Quite-like-thee/318264907152839

I would like a smart logo & business card. The design has to be smart and long lasting. I like simplicity ("less is more"). The image needs to bring over seriousness and style. I target people from 35-65 years old. I would love to have smart warm colours like brown mole or anthracite, eventually with some berry or bordeaux red.

The copy is the following:
Quite like thee
Doreen Pavlik
Mobile: +27 72 463 08 29
eMail: pavlik.doreen@brightmailbox.net
Cape Town

Reason: I'm not in a rush.

Target Market(s)

Core target group: 35-65 years old women; wealthy; living in Cape Town
Larger target group: South Africa; eventually men too

Industry/Entity Type

Business

```html
<!DOCTYPE html>
<html lang="en">
<head>
<meta charset="utf-8">
<title>Doreen Pavlik – Personal Stylist</title>
<link rel="stylesheet" href="https://fonts.googleapis.com/css2?family=Sorts+Mill+Goudy:ital@0;1&display=swap">
<style>
  :root {
    --mole: #735246;
    --mole-deep: #5b4138;
    --ivory: #fbf6f1;
    --ink: #6a4a3f;
    --frame: #1f1f1f;
    --sky-left: #c7ddf4;
    --sky-right: #dde3ea;
  }
  html, body {
    margin: 0;
    padding: 0;
    width: 1200px;
    height: 727px;
    overflow: hidden;
    background: #ffffff;
  }
  .card {
    position: relative;
    width: 1200px;
    height: 727px;
    box-sizing: border-box;
    border: 3px solid var(--frame);
    background: var(--mole);
    overflow: hidden;
    font-family: "Sorts Mill Goudy", "Goudy Old Style", Georgia, serif;
  }
  .brand-backdrop {
    position: absolute;
    left: 8px;
    top: 110px;
    margin: 0;
    font-size: 172px;
    font-weight: 400;
    line-height: 1;
    white-space: nowrap;
    color: var(--mole-deep);
    letter-spacing: 2px;
  }
  .identity {
    position: absolute;
    left: 0;
    right: 0;
    top: 422px;
    text-align: center;
    color: var(--ivory);
  }
  .identity__name {
    margin: 0;
    font-size: 46px;
    font-weight: 400;
    font-variant: small-caps;
    letter-spacing: 1px;
    line-height: 1;
  }
  .identity__role {
    margin: 14px 0 0;
    font-size: 33px;
    font-style: italic;
    line-height: 1;
  }
  .contact-band {
    position: absolute;
    left: 0;
    right: 0;
    bottom: 0;
    height: 117px;
    background: linear-gradient(90deg, var(--sky-left), var(--sky-right));
    display: flex;
    align-items: center;
    justify-content: center;
    gap: 10px;
    color: var(--ink);
    font-size: 34px;
    white-space: nowrap;
  }
  .contact-band__icon {
    width: 44px;
    height: 44px;
    flex: none;
  }
  .contact-band__sep {
    margin: 0 2px;
  }
</style>
</head>
<body>
  <main class="card">
    <p class="brand-backdrop">Quite like thee</p>

    <section class="identity">
      <h1 class="identity__name">Doreen Pavlik</h1>
      <p class="identity__role">Personal Stylist</p>
    </section>

    <footer class="contact-band">
      <svg class="contact-band__icon" viewBox="0 0 44 44" aria-hidden="true">
        <circle cx="22" cy="22" r="19" fill="none" stroke="var(--ink)" stroke-width="2.5"/>
        <path d="M17 11 q-5 3 -3 12 q3 9 11 11 q3 0 4 -2 l-3 -5 q-2 1 -3 0 q-4 -3 -5 -9 q0 -2 2 -2 z"
              fill="none" stroke="var(--ink)" stroke-width="2" stroke-linejoin="round"/>
      </svg>
      <span class="contact-band__phone">+27 72 463 08 29</span>
      <span class="contact-band__sep">-</span>
      <span class="contact-band__city">Cape Town</span>
      <span class="contact-band__sep">-</span>
      <svg class="contact-band__icon" viewBox="0 0 44 44" aria-hidden="true">
        <rect x="3" y="9" width="38" height="26" fill="none" stroke="var(--ink)" stroke-width="3"/>
        <path d="M3 9 L22 25 L41 9 M3 35 L17 21 M41 35 L27 21" fill="none" stroke="var(--ink)" stroke-width="2.5"/>
      </svg>
      <span class="contact-band__email">pavlik.doreen@brightmailbox.net</span>
    </footer>
  </main>
</body>
</html>
```